Corporate Design (Wort-Bildmarke, Visitenkarten, Briefpapier, ppt-Master) für Beratungs-Start-Up
Zielgruppe
Lichtungwerk ist ein Beratungs-Start-Up und bietet Dienstleistungen im Bereich Sales- und Kommunikationsberatung.
Zielgruppe: kleine und mittelständische Unternehmen. Zunächst beschränkt sich Lichtungwerk auf Unternehmen aus dem Fahrrad- & Outdoor- beziehungsweise Uhrenfachhandel.
Beobachten steht für Lichtungwerk im Mittelpunkt. Lichtungwerk steht für Expertenwissen, nicht Besserwissen. Lichtungwerk ist Handwerk, mit einem qualitativ sehr guten, aber leicht verständlichen Ergebnis.
Stichworte für Lichtungwerk sind: offene Türen, Voraussicht, Mut, Elan, Neugier, Unangepasstheit, Optimismus, Originalität, Kreativität, Stärke, Attraktivität, Aktivität und Wandel.
Lichtungwerk ist: Energievoll, Leistungssteigernd, Beweglich, Aufbauend, (Quick)Lebendig, Greifbar, Flexibel, am Puls der Zeit.
Aufgabenstellung
Ich suche ein CD das folgende Punkte umfasst:
- Wort-/Bildmarke
- Briefpapier
- Visitenkarten (einen Vorschlag/Ansatz für einen spannenden haptischen Eindruck fände ich cool!)
- ppt-Master (inkl. Schrift und Farben) mit 3-5 Beispielsweisen (Tabellen, Graphiken, Bubbles oder ähnlichem)
Insgesamt soll das Design schnörkellos sein!
Lichtungwerk ist ein seriöser Ansatz - zwar sportlich und am Puls der Zeit. Steht aber doch eben auch für Vertrauen! Vielleicht so wie ich (siehe Bild unten!)
Im Logo sollten weder ein Fahrrad noch eine Uhr auftauchen.

```html
<!DOCTYPE html>
<html lang="de">
<head>
<meta charset="utf-8">
<title>Lichtungwerk – Geschäftsausstattung</title>
<link rel="stylesheet" href="https://fonts.googleapis.com/css2?family=Oswald:wght@400;500&family=Open+Sans:wght@400;700&display=swap">
<style>
  :root{
    --brand-blue:#005a87;
    --ink:#333336;
    --paper:#ffffff;
    --backdrop:#2a2a2c;
    --rule:#8a8a8a;
  }
  *{margin:0;padding:0;box-sizing:border-box}
  html,body{width:1200px;height:849px;overflow:hidden;background:var(--backdrop)}
  .canvas{position:relative;width:1200px;height:849px}

  /* Letterhead */
  .letterhead{position:absolute;left:129px;top:64px;width:510px;height:721px;background:var(--paper);overflow:hidden;
    font-family:"Open Sans",sans-serif;color:var(--ink);box-shadow:0 6px 14px rgba(0,0,0,.45)}
  .brand{position:absolute;display:flex;align-items:center;gap:6px;font-family:"Oswald",sans-serif;font-weight:500;
    color:var(--ink);letter-spacing:.02em;text-transform:uppercase;white-space:nowrap}
  .brand-square{display:block;background:var(--brand-blue)}
  .letterhead .brand{right:37px;top:38px;font-size:17px}
  .letterhead .brand-square{width:13px;height:13px}
  .return-line{position:absolute;left:55px;top:112px;font-size:5px;padding-bottom:1px;border-bottom:.6px solid var(--rule);width:151px}
  .recipient{position:absolute;left:56px;top:134px;font-size:8px;line-height:10.5px}
  .recipient .city{margin-top:9px}
  .subject{position:absolute;left:56px;top:246px;font-size:7.3px;font-weight:700}
  .body-text{position:absolute;left:56px;top:273px;width:280px;font-size:7px;line-height:9.3px}
  .body-text p+p{margin-top:9px}
  .closing{position:absolute;left:56px;top:514px;font-size:7.3px}
  .signature{position:absolute;left:56px;top:535px;width:106px;height:20px;background:#e9ecee}
  .footer-rule{position:absolute;left:55px;top:662px;width:305px;height:.7px;background:var(--rule)}
  .footer-col{position:absolute;top:675px;font-family:"Oswald",sans-serif;font-size:4.6px;line-height:8.5px;
    text-transform:uppercase;letter-spacing:.05em}
  .footer-col.company{left:55px}
  .footer-col.contact{left:166px}
  .footer-col.bank{left:280px}
  .bullet{display:inline-block;width:4px;height:4px;background:var(--brand-blue);transform:rotate(45deg);margin-right:3px;vertical-align:middle}
  .corner-mark{position:absolute;right:0;bottom:0}

  /* Business card */
  .card{position:absolute;width:259px;height:167px;overflow:hidden;box-shadow:0 5px 12px rgba(0,0,0,.5)}
  .card-front{left:778px;top:189px;background:var(--paper);color:var(--ink)}
  .card-front .brand{left:20px;top:28px;font-size:21px;gap:7px}
  .card-front .brand-square{width:22px;height:22px}
  .card-details{position:absolute;left:68px;top:72px;font-family:"Oswald",sans-serif;font-size:6.8px;line-height:9.8px;
    text-transform:uppercase;letter-spacing:.06em}
  .card-details .name{font-weight:500}
  .card-details .dot{color:var(--brand-blue)}
  .card-details .phones{margin-top:3px}
  .card-details .web{margin-top:3px;color:var(--brand-blue);font-weight:500}
  .card-details .bullet{width:4.5px;height:4.5px}
  .card-back{left:776px;top:493px;background:var(--brand-blue);display:flex;align-items:center;justify-content:center}
  .card-back .brand{position:static;color:var(--paper);font-size:20px}
  .card-back .brand-square{width:18px;height:18px;background:var(--paper)}
</style>
</head>
<body>
<main class="canvas">

  <article class="letterhead">
    <div class="brand"><span class="brand-square"></span>Lichtungwerk</div>

    <div class="return-line">Vorname Nachname, Musterstr. 123, 12345 Musterstadt</div>
    <address class="recipient" style="font-style:normal">
      Martina Musterfrau<br>Musterstraße 456
      <div class="city">12345 Berlin</div>
    </address>

    <h2 class="subject">Quidero molore, atatur sae. Nequat,</h2>

    <div class="body-text">
      <p>Ur sit, imus, ipicatem voluptate eum re dolluptios sequosam, eum reritati am volor sapedissi quo blaboribust, sequass itasped igendi cus exerfer feruptas iusanda ndaest, qui omnis nus aut fugitinis quatur ad ullaut mostem quasperiae corem et aciatem illatin ciduntores quidis utemquam autemperae soluptiae lab illacescia solorum et fugiam ratatatus exerro blaciis samusam etur? Uga. Neque nam simi, nest, ommod essedios magnatia nossi aute nonsequam fugiaspis moluptas sed el int etur saepe nonsecatem excea noneceperrum ulligendit faccullores et lantur si ium at.Ota cuptae non ea de opta voles rem rae dolore ilia vellab isi blanis idit veribus auda alit labore desenis imenis que in con rehent, explat ped que volorum, autent, si tetur?</p>
      <p>Ihil ium restior ecepero reptistius es aborepe diatiunt dignis diciae voluptu ribearit, que nat aute et as maximus, qui blab iur aut volest, nonsequae odios doluptatiae velignimin perescia vent.<br>Pa voluptas expero corectur molest eaquid enda vidus verciis quodi te dit aliquid unturem poreper feratur? Quis aut rehenihilit et quam, eris et perorru mquamusa quo et untia volupie nisimoluptae esseribus cora doluptati doluptatur atisciumqui re pa quat aut lam solescia intiis et millabor sit odis et quos re sam, vendicientur abo. Equi totatus rest, nosam quodi omni doloriosam des ea nimpelique volo elendae dellign ihilitis solupta temporp orupta iuntia ipiste natibusapis volesedis reriori taerrup tatiberes nobitiur, sequi omnihillab id maximagnat omnimus dolo quunt, int aut earum lacit peliquunt iduciet, id que autemolum deruptati te non re.</p>
    </div>

    <div class="closing">Sincerely</div>
    <div class="signature" role="img" aria-label="Handschriftliche Unterschrift"></div>

    <div class="footer-rule"></div>
    <div class="footer-col company">Musterfirma GmbH<br>Musterstr. 123<br>12345 Musterstadt</div>
    <div class="footer-col contact"><span class="bullet"></span>010 / 234 567 89<br><span class="bullet"></span>010 / 234 567 90<br><span class="bullet"></span>info@beispielnetz.de</div>
    <div class="footer-col bank">Musterbank AG<br>IBAN: DE12 3456 7890 1234<br>BIC: ABC456789</div>

    <svg class="corner-mark" width="110" height="110" viewBox="0 0 110 110" aria-hidden="true">
      <polygon points="61,0 122,61 61,122 0,61" fill="var(--brand-blue)"/>
    </svg>
  </article>

  <section class="card card-front">
    <div class="brand"><span class="brand-square"></span>Lichtungwerk</div>
    <div class="card-details">
      <div class="name">Max Mustermann <span class="dot">•</span> Geschäftsführer</div>
      <div>Musterfirma GmbH</div>
      <div>Musterstr. 123 <span class="dot">•</span> 12345 Musterstadt</div>
      <div class="phones"><span class="bullet"></span>010 / 234 567 89 &nbsp;<span class="bullet"></span>010 / 234 567 90</div>
      <div><span class="bullet"></span>info@beispielnetz.de</div>
      <div class="web">www.beispielnetz.de</div>
    </div>
    <svg class="corner-mark" width="54" height="54" viewBox="0 0 54 54" aria-hidden="true">
      <polygon points="28,0 54,26 28,52 2,26" fill="var(--brand-blue)"/>
    </svg>
  </section>

  <section class="card card-back">
    <div class="brand"><span class="brand-square"></span>Lichtungwerk</div>
  </section>

</main>
</body>
</html>
```